Business Card Design needed for logo design project

This project is linked to Veltrix Ember Social Media Logo.

Our company needs a Business Card Design. Please refer to our original project in the link above.

Industry/Entity Type

Business

```html
<!DOCTYPE html>
<html lang="en">
<head>
<meta charset="UTF-8">
<title>Veltrix Ember Business Card</title>
<link href="https://fonts.googleapis.com/css2?family=Questrial&display=swap" rel="stylesheet">
<style>
  :root {
    --page-bg: #e9e6e1;
    --card-bg: #2d2d2e;
    --accent-blue: #4a88c8;
    --text-white: #ffffff;
    --text-soft: #d4d4d4;
  }
  * { margin: 0; padding: 0; box-sizing: border-box; }
  html, body { width: 1200px; height: 900px; overflow: hidden; }
  body {
    background: var(--page-bg);
    font-family: "Questrial", "Century Gothic", sans-serif;
    position: relative;
  }
  .card {
    position: absolute;
    width: 600px;
    height: 343px;
    background: var(--card-bg);
    box-shadow: 0 14px 30px rgba(0,0,0,0.28);
    overflow: hidden;
  }
  .card-back { left: 470px; top: 50px; }
  .card-front { left: 130px; top: 480px; }

  .brand {
    position: absolute;
    display: flex;
    align-items: center;
    gap: 12px;
  }
  .brand-square {
    width: 34px; height: 34px;
    background: var(--text-white);
  }
  .brand-name {
    color: var(--text-white);
    font-size: 30px;
    letter-spacing: 1px;
    text-transform: uppercase;
    line-height: 1;
  }
  .card-back .brand { left: 190px; top: 130px; }
  .tagline {
    position: absolute;
    left: 236px; top: 172px;
    color: var(--text-white);
    font-size: 10px;
  }
  .back-web {
    position: absolute;
    left: 190px; top: 220px;
    color: var(--text-white);
    font-size: 17px;
    letter-spacing: 6px;
  }

  .name-band {
    position: absolute;
    left: 0; top: 36px;
    width: 330px; height: 66px;
    background: var(--accent-blue);
    padding: 10px 0 0 48px;
    color: var(--text-white);
  }
  .person-name { font-size: 22px; line-height: 1.1; }
  .person-role { font-size: 13px; margin-top: 4px; }

  .card-front .brand { left: 346px; top: 52px; }

  .address {
    position: absolute;
    left: 48px; top: 132px;
    color: var(--text-soft);
    font-size: 15px;
    line-height: 1.45;
  }
  .contact-list {
    position: absolute;
    left: 48px; top: 196px;
    list-style: none;
    color: var(--text-soft);
    font-size: 15px;
  }
  .contact-list li {
    display: flex;
    align-items: center;
    gap: 10px;
    height: 24px;
  }
  .contact-icon { width: 14px; height: 14px; flex: none; }
</style>
</head>
<body>
  <section class="card card-back">
    <div class="brand">
      <span class="brand-square"></span>
      <span class="brand-name">Veltrix Ember</span>
    </div>
    <p class="tagline">Your Trusted Real Estate Advisors</p>
    <p class="back-web">www.veltrixember.com</p>
  </section>

  <section class="card card-front">
    <div class="name-band">
      <p class="person-name">Mara Ellison</p>
      <p class="person-role">Director</p>
    </div>
    <div class="brand">
      <span class="brand-square"></span>
      <span class="brand-name">Veltrix Ember</span>
    </div>
    <p class="address">Suite 214 Harbor Lane<br>Bay State, Zip 4071, County</p>
    <ul class="contact-list">
      <li>
        <svg class="contact-icon" viewBox="0 0 16 16" aria-hidden="true"><path fill="#4a88c8" d="M3 1h3l1 4-2 1.5a9 9 0 0 0 4.5 4.5L11 9l4 1v3a2 2 0 0 1-2 2C6.5 15 1 9.5 1 3a2 2 0 0 1 2-2z"/></svg>
        127 555 0142
      </li>
      <li>
        <svg class="contact-icon" viewBox="0 0 16 16" aria-hidden="true"><rect x="1" y="4" width="14" height="10" rx="1" fill="#4a88c8"/><rect x="4" y="1" width="8" height="5" fill="#4a88c8"/><rect x="4" y="9" width="8" height="3" fill="#2d2d2e"/></svg>
        345 555 0188
      </li>
      <li>
        <svg class="contact-icon" viewBox="0 0 16 16" aria-hidden="true"><rect x="1" y="3" width="14" height="10" fill="#4a88c8"/><path d="M1 3l7 6 7-6" fill="none" stroke="#2d2d2e" stroke-width="1.4"/></svg>
        hello@veltrixember.com
      </li>
      <li>
        <svg class="contact-icon" viewBox="0 0 16 16" aria-hidden="true"><circle cx="8" cy="8" r="7" fill="#4a88c8"/><path d="M1 8h14M8 1c-3 3-3 11 0 14M8 1c3 3 3 11 0 14" fill="none" stroke="#2d2d2e" stroke-width="1"/></svg>
        www.veltrixember.com
      </li>
    </ul>
  </section>
</body>
</html>
```